A-Frame Sign for CPR Training

Summit Readiness Academy provides CPR and First Aid classes to businesses and individuals throughout Northern California. We are in need of a 36in TALL x 24in WIDE poster insert to use on our A-Frame sign. We need the design to include:

1. our logo (see attachment)
2. a border (professional and clean, but catchy)
3. our contact information including phone #: 916-784-3126 and website: www.BlueRiverSkills.example
4. basic product info and price, possibly include a small picture for each?
"CPR - $39" and "BLS" - $49"
5. the phases: "CPR and First Aid Classes" and "Taught by Firefighters" and "Sacramento | Stockton | Modesto"
6. use our theme colors of blue(003399) and green(80cc33)
7. EXTRA CREDIT: somewhere place a small "camera" icon with the words "snap a picture of me for later"

Industry/Entity Type

Training

Font styles to use
Serif

Requirements
Nice to have
• EXTRA CREDIT: somewhere place a small "camera" icon with the words "snap a picture of me for later"

```html
<!DOCTYPE html>
<html lang="en">
<head>
<meta charset="utf-8">
<title>Summit Readiness Academy – CPR + BLS Poster</title>
<link rel="stylesheet" href="https://fonts.googleapis.com/css2?family=Tinos:wght@400;700&display=swap">
<style>
  :root {
    --brand-blue: #0a2a9c;
    --brand-green: #80cc33;
    --ink-navy: #1c2a6e;
    --accent-red: #b3262b;
    --paper: #ffffff;
    --stage: #e9ebee;
    --photo-a: #6f7f95;
    --photo-b: #3b4a63;
  }
  * { box-sizing: border-box; margin: 0; padding: 0; }
  html, body { width: 978px; height: 1200px; overflow: hidden; }
  body { background: var(--stage); font-family: "Tinos", "Times New Roman", serif; }

  .poster {
    position: absolute; left: 76px; top: 0;
    width: 826px; height: 1200px;
    background: var(--paper);
    overflow: hidden;
  }
  .poster__frame { position: absolute; inset: 0; }

  .header { position: absolute; left: 0; top: 0; width: 100%; text-align: center; }
  .header__kicker { position: absolute; top: 32px; width: 100%; font-size: 46px; color: var(--brand-blue); letter-spacing: 1px; }
  .header__title { position: absolute; top: 92px; width: 100%; font-size: 48px; font-weight: 700; color: var(--paper); text-shadow: 1px 2px 3px rgba(0,0,0,.35); letter-spacing: 1px; }
  .header__tagline { position: absolute; top: 152px; width: 100%; font-size: 32px; font-weight: 700; color: var(--accent-red); }

  .course { position: absolute; left: 0; width: 100%; }
  .course--cpr { top: 280px; }
  .course--bls { top: 530px; }
  .course__photo {
    position: absolute; left: 64px; top: 0;
    width: 312px; height: 178px; border-radius: 50%;
    border: 9px solid var(--brand-green);
    box-shadow: 0 0 0 7px var(--brand-blue);
    background: linear-gradient(135deg, var(--photo-a), var(--photo-b));
  }
  .course__info { position: absolute; left: 448px; top: 16px; width: 300px; }
  .course__name { font-size: 29px; font-weight: 700; color: var(--brand-blue); margin-bottom: 8px; }
  .course__desc { font-size: 19px; line-height: 1.3; color: var(--ink-navy); }

  .contact {
    position: absolute; right: 82px; top: 800px; width: 560px;
    text-align: right; color: var(--brand-blue);
  }
  .contact p { white-space: nowrap; }
  .contact__name { font-size: 36px; line-height: 44px; margin-bottom: 44px; }
  .contact__mark { display: inline-block; width: 28px; height: 28px; border-radius: 50%; background: var(--brand-green); vertical-align: -3px; margin-right: 10px; }
  .contact__line { font-size: 29px; line-height: 42px; }
  .contact__web { font-size: 31px; line-height: 42px; font-weight: 700; }

  .locations { position: absolute; left: 0; top: 1056px; width: 100%; text-align: center; font-size: 40px; color: var(--brand-blue); word-spacing: 6px; }

  .snap { position: absolute; left: 0; top: 1148px; width: 100%; display: flex; justify-content: center; align-items: center; gap: 14px; font-size: 20px; color: var(--ink-navy); }
</style>
</head>
<body>
  <main class="poster">
    <svg class="poster__frame" width="826" height="1200" viewBox="0 0 826 1200" aria-hidden="true">
      <path d="M0 0 H826 V150 C600 200 300 250 0 245 Z" fill="var(--brand-green)"/>
      <path d="M0 245 C300 250 600 200 826 150 V168 C600 220 300 262 0 262 Z" fill="var(--brand-blue)"/>
      <path d="M0 1125 C300 1105 600 1105 826 1125 V1200 H0 Z" fill="var(--brand-green)"/>
      <path d="M0 1125 C300 1105 600 1105 826 1125 V1133 C600 1113 300 1113 0 1133 Z" fill="var(--brand-blue)"/>
    </svg>

    <header class="header">
      <p class="header__kicker">ENROL NOW</p>
      <h1 class="header__title">CPR + BLS</h1>
      <p class="header__tagline">Weekly classes taught by Firefighters</p>
    </header>

    <section class="course course--cpr">
      <div class="course__photo" role="img" aria-label="Photo of a CPR class practising chest compressions on a manikin"></div>
      <div class="course__info">
        <h2 class="course__name">CPR -$39</h2>
        <p class="course__desc">For the general public, this course includes the latest National Cardiac Council Guidelines on how to provide CPR for an Adult, Child and Infant.</p>
      </div>
    </section>

    <section class="course course--bls">
      <div class="course__photo" role="img" aria-label="Photo of healthcare providers practising basic life support"></div>
      <div class="course__info">
        <h2 class="course__name">BLS - $49</h2>
        <p class="course__desc">For Healthcare Providers, this course provides knowledge and skills on how to provide Basic Life Support to all ages.</p>
      </div>
    </section>

    <section class="contact">
      <p class="contact__name"><span class="contact__mark"></span>Summit Readiness Academy</p>
      <p class="contact__line">Phone: 916-784-3126</p>
      <p class="contact__line">Email: info@sracpr.example</p>
      <p class="contact__web">www.BlueRiverSkills.example</p>
    </section>

    <p class="locations">Sacramento &nbsp;|&nbsp; Stockton &nbsp;|&nbsp; Modesto</p>

    <p class="snap">
      <svg width="32" height="26" viewBox="0 0 32 26" aria-hidden="true">
        <rect x="1" y="5" width="30" height="20" rx="3" fill="var(--brand-blue)"/>
        <rect x="10" y="1" width="12" height="6" rx="1.5" fill="var(--brand-blue)"/>
        <circle cx="16" cy="15" r="6.5" fill="var(--paper)"/>
        <circle cx="16" cy="15" r="4" fill="var(--brand-blue)"/>
      </svg>
      <span>snap a picture of me for later</span>
    </p>
  </main>
</body>
</html>
```